Web design for consulting advisory business company

We need a web for our business consulting company. The web should transmit simplicity, innovation, trust, and solid knowledge of what we do. Inspirational webs to take a look are: https://brindlemont.com/ and http://taviresul.com.br. Use blue colors.

Target Market(s)

Private companies

Industry/Entity Type

Management Consulting

Number of Pages Required

5+ page

Font styles to use
Serif
Sans Serif

Colors
3176b5
3276b5
85abd2
85cae6
33a6d7
0592cd
ffffff
1b1b1b
474747

Requirements
Must have
• - use of blue
• - images
• - same version in different languages (portugueses and spanish)
Nice to have
• - white as background

```html
<!DOCTYPE html>
<html lang="pt">
<head>
<meta charset="utf-8">
<title>Veloria Partners – Consulting Advisory</title>
<link href="https://fonts.googleapis.com/css2?family=Lato:wght@300;400;700;900&display=swap" rel="stylesheet">
<style>
:root{
  --blue:#3176b5;
  --blue-bright:#0592cd;
  --blue-sky:#33a6d7;
  --blue-soft:#85abd2;
  --blue-pale:#85cae6;
  --ink:#1b1b1b;
  --graphite:#474747;
  --white:#ffffff;
  --muted:#777;
  --line:#e4e4e4;
}
*{box-sizing:border-box;margin:0;padding:0}
html,body{width:1200px;height:5085px;overflow:hidden}
body{font-family:'Lato',sans-serif;color:var(--ink);background:var(--white);position:relative}
.section-title{font-size:34px;font-weight:700;text-align:center;color:var(--ink)}
.section-lead{width:780px;margin:28px auto 0;text-align:center;font-size:13px;line-height:22px;color:var(--muted)}
.btn{display:inline-block;font-weight:900;font-size:14px;letter-spacing:1.5px;padding:0;text-align:center}

/* nav */
.topbar{height:120px;display:flex;align-items:center;padding:0 95px}
.brand{display:flex;align-items:center;gap:10px;font-weight:900;font-size:26px;color:var(--blue);letter-spacing:1px}
.brand-square{width:30px;height:30px;background:var(--blue)}
.nav{display:flex;gap:26px;margin-left:auto;font-size:13px;font-weight:700;letter-spacing:.5px}
.lang{margin-left:34px;border:1px solid #bbb;padding:7px 12px;font-size:13px;font-weight:700}

/* hero */
.hero{height:490px;display:flex}
.hero-photo{width:815px;background:linear-gradient(120deg,#cfd9e2,#8fa5b8 55%,#5d7589)}
.hero-panel{flex:1;background:var(--blue-bright);color:var(--white);padding:58px 50px}
.hero-title{font-size:48px;font-weight:900;line-height:54px}
.hero-sub{font-size:22px;margin-top:10px}
.hero-text{font-size:14px;line-height:21px;margin-top:34px;width:260px}
.hero-cta{margin-top:30px;background:var(--ink);color:var(--white);width:236px;height:66px;line-height:66px}

/* principles */
.principles{height:305px;padding-top:62px}
.principles .section-title{color:var(--blue)}
.pillars{height:170px;display:flex}
.pillar{flex:1;display:flex;align-items:center;justify-content:center;gap:18px;color:var(--white);font-size:28px;font-weight:700;line-height:32px}
.pillar:nth-child(1){background:var(--blue)}
.pillar:nth-child(2){background:var(--blue-bright)}
.pillar:nth-child(3){background:#2f6aa5}

/* expertise */
.expertise{height:305px;padding-top:72px}
.expertise-grid{height:390px;display:flex}
.area{flex:1;padding:42px 46px;color:var(--white);position:relative}
.area:nth-child(odd){background:var(--ink)}
.area:nth-child(2){background:var(--graphite)}
.area h3{font-size:27px;font-weight:700;line-height:33px;height:70px}
.area ul{list-style:none;font-size:15px;line-height:30px;margin-top:4px}
.area .btn{position:absolute;left:46px;bottom:60px;width:232px;height:66px;line-height:66px;background:var(--white);color:var(--ink)}

/* cases */
.cases{height:255px;padding-top:70px}
.cases-grid{display:grid;grid-template-columns:repeat(3,1fr);grid-template-rows:205px 235px 205px 235px}
.case-photo{background:linear-gradient(135deg,#9fb0bf,#56697b)}
.case-photo.dark{background:linear-gradient(135deg,#27435e,#0d1a28)}
.case-photo.warm{background:linear-gradient(135deg,#b9a48d,#6e5a48)}
.case-text{padding:38px 46px;font-size:15px;line-height:22px}
.case-text.blue{background:var(--blue-bright);color:var(--white)}
.more{height:155px;display:flex;align-items:center;justify-content:center}
.more .btn{background:var(--ink);color:var(--white);width:236px;height:66px;line-height:66px}

/* ecosystem */
.ecosystem{height:545px;padding-top:56px;background:var(--white);border-top:1px solid var(--line)}
.partners{display:flex;justify-content:space-between;padding:0 40px;margin-top:70px}
.partner{width:210px;text-align:center}
.partner-name{height:70px;display:flex;align-items:center;justify-content:center;font-size:34px;font-weight:900;color:var(--ink)}
.partner-name.blue{color:var(--blue)}
.partner p{margin-top:14px;font-size:13px;line-height:19px;color:var(--muted)}

/* team */
.team{height:645px;padding-top:70px;background:#f4f4f4}
.team-grid{display:flex;justify-content:center;gap:40px;margin-top:60px}
.member{width:272px;background:var(--white);text-align:center;padding-bottom:28px}
.member-photo{height:200px;background:linear-gradient(160deg,#e5e8ec,#aeb7c0)}
.member h4{font-size:21px;font-weight:700;margin-top:22px}
.member p{font-size:13px;line-height:19px;color:var(--muted);margin:14px 30px 0;height:76px}
.socials{display:flex;justify-content:center;gap:10px;margin-top:18px}
.socials span{width:24px;height:24px;border-radius:50%;background:var(--blue-sky)}

/* footer */
.footer{height:845px;display:flex}
.offices{width:600px;background:var(--ink);color:var(--white);padding:58px 90px}
.offices h2,.contact h2{font-size:26px;font-weight:400}
.office{display:flex;gap:22px;margin-top:54px}
.office h5{font-size:16px;font-weight:700;margin-bottom:6px}
.office p{font-size:15px;line-height:23px}
.contact{flex:1;background:var(--blue);color:var(--white);padding:58px 70px}
.contact h2{font-weight:700}
.contact p{font-size:14px;line-height:21px;margin-top:32px}
.contact p + p{margin-top:24px}
.contact u{font-weight:700}
.field{height:56px;background:#e9eef4;margin-top:18px;color:#777;font-size:14px;padding:18px 18px}
.field:first-of-type{margin-top:36px}
.field.area-msg{height:120px}
.submit{margin-top:22px;background:var(--ink);color:var(--white);height:60px;line-height:60px;width:100%}
</style>
</head>
<body>

<header class="topbar">
  <div class="brand"><span class="brand-square"></span>VELORIA PARTNERS</div>
  <nav class="nav"><span>PRINCÍPIOS</span><span>EXPERTISE</span><span>CASES</span><span>ECOSISTEMA</span><span>EQUIPE SÊNIOR</span><span>CONTATO</span></nav>
  <div class="lang">POR ▾</div>
</header>

<section class="hero">
  <div class="hero-photo" role="img" aria-label="Foto de executivos sorrindo em reunião de negócios"></div>
  <div class="hero-panel">
    <h1 class="hero-title">Veloria<br>Partners</h1>
    <div class="hero-sub">Consulting Advisory</div>
    <p class="hero-text">Lorem ipsum dolor sit amet, conse ctetur adipiscing elit, sed do.</p>
    <div class="btn hero-cta">LEARN MORE</div>
  </div>
</section>

<section class="principles">
  <h2 class="section-title">Princípios</h2>
  <p class="section-lead">Adaptamos a equipe e os esforços para o problema, combinando recursos seniores e especialistas do setor com fortes recursos analíticos para fornecer soluções sustentáveis. Ouvimos atentamente os nossos clientes e combinamos as nossas equipes com as suas necessidades. Se o escopo do projeto mudar, mudamos a configuração. Pensamos na implementação desde o primeiro dia e permitimos que os líderes com quem trabalhamos mobilizem seu pessoal.</p>
</section>

<section class="pillars">
  <div class="pillar">
    <svg width="34" height="34" viewBox="0 0 34 34" fill="none" stroke="#fff" stroke-width="3"><path d="M17 2v30M2 17h30M12 7l5-5 5 5M12 27l5 5 5-5M7 12l-5 5 5 5M27 12l5 5-5 5"/></svg>
    <span>Flexibilidade</span>
  </div>
  <div class="pillar">
    <svg width="44" height="30" viewBox="0 0 44 30" fill="#fff"><circle cx="22" cy="8" r="6"/><circle cx="9" cy="11" r="4.5"/><circle cx="35" cy="11" r="4.5"/><path d="M12 28c0-7 4-11 10-11s10 4 10 11zM1 28c0-5 3-8 8-8 2 0 3 .5 4 1-2 2-3 4-3 7zM43 28c0-5-3-8-8-8-2 0-3 .5-4 1 2 2 3 4 3 7z"/></svg>
    <span>Co-criação<br>com o cliente</span>
  </div>
  <div class="pillar">
    <svg width="26" height="36" viewBox="0 0 26 36" fill="#fff"><path d="M13 1C6 1 1 6 1 12.5c0 4.5 2.5 7 4.5 9.5 1.2 1.5 1.5 3 1.5 4h12c0-1 .3-2.5 1.5-4 2-2.5 4.5-5 4.5-9.5C25 6 20 1 13 1z"/><rect x="7" y="28" width="12" height="3"/><rect x="9" y="32" width="8" height="3"/></svg>
    <span>Resultados<br>sustentáveis</span>
  </div>
</section>

<section class="expertise">
  <h2 class="section-title">Expertise</h2>
  <p class="section-lead">Um núcleo de recursos seniores, combinado com especialistas do setor, garante resultados sustentáveis para nossos clientes. Não adaptamos a equipe e os esforços para cada situação e criamos impacto através de insights e orientação para as pessoas. Quando solicitado, nos juntamos a especialistas e pioneiros de todos os cantos do mundo.</p>
</section>

<section class="expertise-grid">
  <div class="area">
    <h3>Bens de Consumo</h3>
    <ul><li>Varejo</li><li>Serviços Financeiros</li><li>Saúde</li></ul>
    <div class="btn">READ MORE</div>
  </div>
  <div class="area">
    <h3>TelCo &amp; Mídia</h3>
    <ul><li>Indústria</li></ul>
    <div class="btn">READ MORE</div>
  </div>
  <div class="area">
    <h3>Esportes e Grandes Eventos</h3>
    <ul><li>Transporte &amp; Logística</li><li>Energia &amp; Meio Ambiente</li><li>Energia &amp; Meio Ambiente</li></ul>
    <div class="btn">READ MORE</div>
  </div>
</section>

<section class="cases">
  <h2 class="section-title">Cases</h2>
  <p class="section-lead">A nossa equipe sênior tem ampla experiência em projetos de alto impacto. Algumas dessas experiências incluem:</p>
</section>

<section class="cases-grid">
  <div class="case-photo" role="img" aria-label="Foto de equipe em sala de reunião"></div>
  <div class="case-photo warm" role="img" aria-label="Foto de mesa com notas adesivas de planejamento"></div>
  <div class="case-photo" role="img" aria-label="Foto de colegas discutindo um projeto"></div>
  <div class="case-text">Identificação das principais sinergias, elaboração do modelo de negócios e do plano de integração de duas Grandes Instituições Financeiras Brasileiras; coordenação e acompanhamento da implementação do PMO (Project Management Office)</div>
  <div class="case-text blue">Desenvolvimento do orçamento anual e plano de investimento trienal para Grande Empresa Brasileira de Serviços Financeiros, identificando oportunidades de melhoria de 8% do orçamento total</div>
  <div class="case-text">Reestruturação da organização de vendas e revisão das políticas comerciais de Empresas Farmacêuticas e de Mídia Online com operações no Brasil</div>
  <div class="case-photo" role="img" aria-label="Foto de profissional trabalhando no notebook"></div>
  <div class="case-photo dark" role="img" aria-label="Foto de silhuetas em reunião contra janela"></div>
  <div class="case-photo" role="img" aria-label="Foto de mãos sobre documentos e gráficos"></div>
  <div class="case-text blue">Otimização do modelo operacional e tributário para empresa Européia líder de alimentos com operações no Brasil</div>
  <div class="case-text">Revisão do modelo operacional de Empresa Líder de Telecomunicações com operações na Europa e na América Latina, a fim de preparar a organização para um IPO</div>
  <div class="case-text blue">Elaboração de nova oferta e plano de negócios para grande instituição financeira no Brasil</div>
</section>

<div class="more"><div class="btn">VIEW MORE</div></div>

<section class="ecosystem">
  <h2 class="section-title">Ecosistema</h2>
  <p class="section-lead">Nos juntamos a especialistas globais e pioneiros de todo o mundo. A necessidade de saturidade e complexidade de problemas exige uma abordagem flexível, e nosso ecossistema oferece acesso a conhecimento exclusivo de líderes da indústria de classe mundial.</p>
  <div class="partners">
    <div class="partner"><div class="partner-name">Norvik</div><p>rede global com mais de 500 mil experts independentes de variadas indústrias</p></div>
    <div class="partner"><div class="partner-name blue">Pollfield</div><p>rede global de especialistas comportamentais</p></div>
    <div class="partner"><div class="partner-name">Lumenforge</div><p>instituto de pesquisa</p></div>
    <div class="partner"><div class="partner-name">Quantara</div><p>plataforma de inteligência artificial e prestador de serviços</p></div>
    <div class="partner"><div class="partner-name blue">Tessaline</div><p>solução de ponta a ponta para inovações de Internet of Things</p></div>
  </div>
</section>

<section class="team">
  <h2 class="section-title">Equipe Sênior</h2>
  <div class="team-grid">
    <div class="member">
      <div class="member-photo" role="img" aria-label="Retrato de João Teixeira"></div>
      <h4>João Teixeira</h4>
      <p>Lorem ipsum dolor sit amet, consectetur adipiscing elit, sed do eiusmod tempor incididunt ut labore et dolore magna aliqua. Ut enim ad minim veniam.</p>
      <div class="socials"><span></span><span></span></div>
    </div>
    <div class="member">
      <div class="member-photo" role="img" aria-label="Retrato de Ramon Albuquerque"></div>
      <h4>Ramon Albuquerque</h4>
      <p>Administrador de Empresas pela Universidade de Montevale (UMV) e Master em Business Administration (MBA) pela Halloran Business School.</p>
      <div class="socials"><span></span><span></span></div>
    </div>
    <div class="member">
      <div class="member-photo" role="img" aria-label="Retrato de Alejandro Ferrer"></div>
      <h4>Alejandro Ferrer</h4>
      <p>Lorem ipsum dolor sit amet, consectetur adipiscing elit, sed do eiusmod tempor incididunt ut labore et dolore magna aliqua. Ut enim ad minim veniam.</p>
      <div class="socials"><span></span><span></span></div>
    </div>
  </div>
</section>

<footer class="footer">
  <div class="offices">
    <h2>Nossos Escritórios</h2>
    <div class="office">
      <svg width="26" height="34" viewBox="0 0 26 34" fill="#33a6d7"><path d="M13 0C6 0 1 5 1 12c0 9 12 22 12 22s12-13 12-22C25 5 20 0 13 0zm0 17a5 5 0 110-10 5 5 0 010 10z"/></svg>
      <div><h5>Rio de Janeiro</h5><p>Av. das Palmeiras, 418 - 14º andar - Centro<br>Rio de Janeiro | 20031-207 | RJ</p></div>
    </div>
    <div class="office">
      <svg width="26" height="34" viewBox="0 0 26 34" fill="#33a6d7"><path d="M13 0C6 0 1 5 1 12c0 9 12 22 12 22s12-13 12-22C25 5 20 0 13 0zm0 17a5 5 0 110-10 5 5 0 010 10z"/></svg>
      <div><h5>São Paulo</h5><p>Rua dos Ipês, 305 - Torre D, 5º andar - Vila<br>Olímpia São Paulo | 04552-018 | SP</p></div>
    </div>
    <div class="office">
      <svg width="26" height="34" viewBox="0 0 26 34" fill="#33a6d7"><path d="M13 0C6 0 1 5 1 12c0 9 12 22 12 22s12-13 12-22C25 5 20 0 13 0zm0 17a5 5 0 110-10 5 5 0 010 10z"/></svg>
      <div><h5>Buenos Aires</h5><p>Av. de los Álamos 1870 - Olivos<br>Buenos Aires | B1637 DSR | Argentina</p></div>
    </div>
  </div>
  <div class="contact">
    <h2>Avance com confiança</h2>
    <p>Contacte-nos para mais informações sobre como Veloria Partners pode ajudar você a conseguir maiores resultados, otimizar o desempenho e melhorar o crescimento do seu negócio.</p>
    <p>Utilize o formulário de contato abaixo ou envie nos um e-mail diretamente a <u>contato@veloria-partners.com.br</u></p>
    <div class="field">Nome</div>
    <div class="field">Organização</div>
    <div class="field">Telefone</div>
    <div class="field">E-mail</div>
    <div class="field area-msg">Mensagem</div>
    <div class="btn submit">SUBMIT</div>
  </div>
</footer>

</body>
</html>
```